Bright Orchard
Bright & Fun-filled
Talia Brennick
Certified Holistic Wellness Coach, NLP Practitioner
no address pls
talia@brightorchard.com
www.brightorchard.com
To love oneself is the beginning of a lifelong romance. --Edwin Tarrow

```html
<!DOCTYPE html>
<html lang="en">
<head>
<meta charset="utf-8">
<title>Bright Orchard – Business Cards</title>
<link rel="stylesheet" href="https://fonts.googleapis.com/css2?family=Arimo:ital,wght@0,400;0,700;1,400&display=swap">
<style>
  :root {
    --backdrop: #e9e9ec;
    --card-white: #ffffff;
    --card-shade: #ececec;
    --brand-pink: #e8175d;
    --ink-dark: #4a4a4a;
    --ink-body: #555555;
    --heart-pink-soft: #f4a9c2;
    --heart-white-soft: #ffe3ec;
  }
  * { box-sizing: border-box; margin: 0; padding: 0; }
  html, body { width: 1200px; height: 828px; overflow: hidden; }
  body {
    background: var(--backdrop);
    font-family: "Arimo", Arial, sans-serif;
    position: relative;
  }
  .card {
    position: absolute;
    width: 434px;
    height: 262px;
    border-radius: 20px;
    overflow: hidden;
    box-shadow: 0 6px 16px rgba(0,0,0,0.18);
  }
  .card--front-a { left: 149px; top: 176px; }
  .card--front-b { left: 629px; top: 176px; }
  .card--back-pink { left: 149px; top: 461px; background: var(--brand-pink); }
  .card--back-white { left: 629px; top: 461px; }
  .card--front-a, .card--front-b, .card--back-white {
    background: linear-gradient(180deg, var(--card-white) 0%, var(--card-white) 50%, var(--card-shade) 100%);
  }
  .wordmark {
    position: absolute;
    top: 34px;
    left: 84px;
    font-size: 40px;
    font-weight: 400;
    color: var(--ink-dark);
    letter-spacing: -0.5px;
    white-space: nowrap;
    line-height: 1;
  }
  .tagline {
    position: absolute;
    top: 80px;
    left: 86px;
    font-size: 11px;
    color: var(--brand-pink);
    letter-spacing: 0.3px;
    white-space: nowrap;
  }
  .heart-art {
    position: absolute;
    left: 0;
    top: 82px;
    width: 210px;
    height: 180px;
    background: radial-gradient(ellipse at 45% 45%, var(--heart-pink-soft), rgba(244,169,194,0) 70%);
  }
  .contact {
    position: absolute;
    right: 20px;
    top: 124px;
    width: 220px;
    color: var(--ink-body);
    font-size: 10px;
    line-height: 1.35;
    text-align: right;
  }
  .contact__name {
    color: var(--brand-pink);
    font-weight: 700;
    font-size: 14px;
    margin-bottom: 1px;
  }
  .contact__title { margin-bottom: 14px; }
  .contact__web { margin-top: 12px; }
  .center-art {
    position: absolute;
    left: 130px;
    top: 36px;
    width: 180px;
    height: 180px;
    border-radius: 50%;
  }
  .card--back-pink .center-art {
    background: radial-gradient(circle, rgba(255,227,236,0.6), rgba(255,227,236,0) 70%);
  }
  .card--back-white .center-art {
    background: radial-gradient(circle, var(--heart-pink-soft), rgba(244,169,194,0) 70%);
  }
  .quote {
    position: absolute;
    left: 20px;
    right: 20px;
    bottom: 18px;
    font-size: 10px;
    font-style: italic;
    color: var(--ink-body);
    text-align: center;
  }
</style>
</head>
<body>

  <section class="card card--front-a">
    <div class="wordmark">Bright Orchard</div>
    <div class="tagline">Bright &amp; Fun-filled</div>
    <div class="heart-art" role="img" aria-label="Hand-sketched pink heart illustration"></div>
    <div class="contact">
      <p class="contact__name">Talia Brennick</p>
      <p class="contact__title">Certified Holistic Wellness Coach,<br>NLP Practitioner</p>
      <p class="contact__phone">Phone: 555 014 2730</p>
      <p class="contact__email">Email: talia@brightorchard.com</p>
      <p class="contact__web">www.brightorchard.com</p>
    </div>
  </section>

  <section class="card card--front-b">
    <div class="wordmark">Bright Orchard</div>
    <div class="tagline">Bright &amp; Fun-filled</div>
    <div class="heart-art" role="img" aria-label="Hand-sketched pink heart illustration"></div>
    <div class="contact">
      <p class="contact__name">Talia Brennick</p>
      <p class="contact__title">Certified Holistic Wellness Coach,<br>NLP Practitioner</p>
      <p class="contact__phone">Phone: 555 014 2730</p>
      <p class="contact__email">Email: talia@brightorchard.com</p>
      <p class="contact__web">www.brightorchard.com</p>
    </div>
  </section>

  <section class="card card--back-pink">
    <div class="center-art" role="img" aria-label="Hand-sketched white heart illustration"></div>
  </section>

  <section class="card card--back-white">
    <div class="center-art" role="img" aria-label="Hand-sketched pink heart illustration"></div>
    <p class="quote">“To love oneself is the beginning of a lifelong romance.” — Edwin Tarrow</p>
  </section>

</body>
</html>
```